依頼概要
■依頼の目的/概要
・電子書籍(自己啓発系)の表紙デザインをお願いします。
・電子書籍は、ソルベリアで販売します。pagoraです。

■本の内容
・初出版本です。
・行き詰った人生を何とかしたいなら、人間関係の苦しみを解消したいなら…。自分の『あり方』を変えることによって、人生がうまくいく方向に動きだすよ ということをお伝えする内容になっています。
・作者の経験が、本の元になっています。
・働く世代や、実際に苦しんでいる当事者、ひきこもりの子どもを持つ親など、幅広く読んでもらいたいです。

■デザイン要望
・明るい未来を感じられるような表紙デザインにしてください。
(底抜けに明るいのは×だけど、悲壮感が見えるのも×)
・人物や、絵が入っている表紙が望ましいです。
(イラスト・写真〇。文字のみのデザインは、×)

■本のタイトル
・本のタイトルは、

毎日が「疲れた…」と感じる君へ、ひとつずつ笑顔が戻ってくる、小さな灯火の地図

です。

・サブキャッチに

~胸のざわめきの理由は〝本音の迷子〟だった~

を入れてください。

■ごあいさつ
・その他、ご不明な点がありましたらお気軽にご質問ください。よろしくお願いします。

■ 選んだ理由

Talkvineをつかって、皆さんからいただいた仮案をアンケートさせていただいたところ、
もっとも「いい」「好き」という評価をいただけたのが、今回選ばせていただいたデザインでした。

なぜよかったのか? と聞いてみたところ
「右下のキャラクターが可愛い」
「見ていると、癒される」
「澄ちゃん(私のこと)らしい」
という意見が、出そろいました。

正直に申しますと、私自身も意外だったのですが
多くの人から「このデザインがいちばん私らしい」と言っていただけるので、気になりはじめ、
今では私自身も気に入っております。

■ 提案者全員のお礼・コメント

本当にありがとうございました。

たった一つのデザインを決めるために、たくさんの方から頂いたデザインを落とさなければならないため、胸を痛めました。
落とすには、あまりにも私好みのデザインがあり過ぎました。

中には私の、初出版の、あまり上手とはいえない文章を丁寧に読んでくれる方もいらっしゃり、とても嬉しかったです。
ありがとうございます。
感謝しています。

また何かの折、お世話になることがあれば、よろしくお願いいたします。

```html
<!DOCTYPE html>
<html lang="ja">
<head>
<meta charset="utf-8">
<title>小さな灯火の地図</title>
<link rel="stylesheet" href="https://fonts.googleapis.com/css2?family=Noto+Sans+JP:wght@700;900&family=Noto+Serif+JP:wght@600;900&display=swap">
<style>
  :root {
    --ink: #111111;
    --paper: #ffffff;
    --accent-blue: #2f7fc8;
    --accent-red: #e0201b;
    --photo-light: #d9d9d9;
    --photo-dark: #3a3a3a;
    --heart: #d8281f;
  }
  * { margin: 0; padding: 0; box-sizing: border-box; }
  html, body { width: 752px; height: 1200px; overflow: hidden; background: var(--paper); }
  .cover {
    position: relative;
    width: 752px;
    height: 1200px;
    background: var(--paper);
    font-family: "Noto Sans JP", sans-serif;
    color: var(--ink);
    overflow: hidden;
  }
  .photo {
    position: absolute;
    left: 0; top: 560px;
    width: 752px; height: 440px;
    background:
      radial-gradient(ellipse 170px 130px at 360px 220px, var(--heart) 0%, var(--heart) 55%, rgba(216,40,31,0) 100%),
      linear-gradient(180deg, var(--paper) 0%, var(--photo-light) 30%, #9a9a9a 70%, var(--photo-dark) 100%);
  }
  .vertical {
    position: absolute;
    writing-mode: vertical-rl;
    line-height: 1;
    white-space: nowrap;
  }
  .lead {
    right: 24px; top: 44px;
    font-family: "Noto Serif JP", serif;
    font-size: 78px;
    font-weight: 900;
  }
  .emphasis {
    right: 117px; top: 150px;
    padding: 20px 10px;
    background: var(--accent-blue);
    color: var(--paper);
    font-family: "Noto Serif JP", serif;
    font-size: 58px;
    font-weight: 900;
  }
  .phrase {
    font-family: "Noto Serif JP", serif;
    font-weight: 600;
  }
  .phrase-one { right: 210px; top: 150px; font-size: 44px; }
  .phrase-two { right: 266px; top: 150px; font-size: 36px; }
  .title-main {
    right: 330px; top: 46px;
    font-size: 92px;
    font-weight: 900;
  }
  .title-accent {
    right: 444px; top: 160px;
    font-size: 180px;
    font-weight: 900;
    color: var(--accent-red);
  }
  .author {
    position: absolute;
    right: 34px; top: 862px;
    font-family: "Noto Serif JP", serif;
    font-weight: 900;
    font-size: 42px;
  }
  .author small { font-size: 26px; font-weight: 600; }
  .catch-band {
    position: absolute;
    left: 0; bottom: 0;
    width: 752px; height: 200px;
    background: var(--accent-blue);
    color: var(--paper);
    font-family: "Noto Serif JP", serif;
    font-weight: 900;
    text-align: center;
    padding-top: 24px;
  }
  .catch-line { font-size: 46px; line-height: 1.2; }
  .catch-line-second { margin-top: 12px; font-size: 58px; line-height: 1.15; }
  .catch-box {
    display: inline-block;
    background: var(--paper);
    color: var(--accent-blue);
    padding: 0 10px;
  }
</style>
</head>
<body>
<main class="cover">
  <div class="photo" role="img" aria-label="差し出された手が赤い折り紙のハートを受け渡すモノクロ写真"></div>

  <div class="vertical lead">毎日が</div>
  <div class="vertical emphasis">「疲れた…」</div>
  <div class="vertical phrase phrase-one">と感じる君へ</div>
  <div class="vertical phrase phrase-two">ひとつずつ笑顔が戻ってくる</div>
  <h1 class="vertical title-main">小さな灯火の</h1>
  <div class="vertical title-accent">地図</div>

  <p class="author">森川澄子<small>〈著〉</small></p>

  <div class="catch-band">
    <p class="catch-line">胸のざわめきの理由は</p>
    <p class="catch-line catch-line-second"><span class="catch-box">「本音の迷子」</span>だった</p>
  </div>
</main>
</body>
</html>
```